Funky Modern Flyer A5 or Postcard size

Hi, I am looking at a one small flyer (A5 or postcard size) that I can put both on my website on the front page (ie so png) and also send out if necessary.

It has to be modern, funky and hip. My brand is professional / Corporate so it also has to fit in with that brand.

There are 6 attachments:
Example 1 - FernaPeak - I like this look, clean, modern, funky and says it all.
Example 2 - FernPeak - again another look I like, simple, explanatory
Example 4 - Brightstall Bazaar - font is cool on this one but background not so much too much going on but I like the font
Example 5 - Example 4 - Brightstall Bazaar - font is cool on this one but background not so much too much going on but I like the font
5 is my logo
Example 6 is something I found on the web this morning which is effective.

It is for a Mentoring and Training program I run called: HIGHSTRIDE

What is to be included is the following:
The name: Highstride
Somewhere: Training, Mentoring
My Logo (see attached two options) you can choose which colour suits and I have the source file should you need it
My website and email: www.miriambaskell.example / miriam@miriambaskell.example

This wording: This is one of our highest in-demand programs and is based on a background and proven track record by Miriam in accelerating sales organisations and their people into stand out high performers. **(NOTE this wording in this paragraph may change and I am open to you changing if you think you can make it more effective!)

Colours: white, black and gold (those are our website colours).

I'd like the Highstride to really stand out.... I have included two fonts that I really like that I got off Brightstall Bazaar. However, feel free to suggest other fonts that you think cool or funky!
Updates

Hi everyone, just to add a note to the brief, I am not overly keen on pictures that are really busy. I only like a picture that is minimal and effective. The examples from Brightstall Bazaar was more for the Font Style not so much the pictures in the background. The pictures can take away from a design unless done really minimally.....hope this makes sense. Miriam Added Wednesday, March 15, 2017

Target Market(s)

My target Market is Corporates but I want a Funky Modern look as a lot of people in Corporates are Millennials as well which is part of my target market

Industry/Entity Type

Information Technology

Requirements
Must have
• What is to be included is the following:
• The name: Highstride
• Somewhere: Training, Mentoring
• My Logo (see attached two options) you can choose which colour suits and I have the source file should you need it
• My website and email: www.miriambaskell.example / miriam@miriambaskell.example
• This wording: This is one of our highest in-demand programs and is based on a background and proven track record in high performance and accelerating sales organisations and their people into stand out high performers. (**NOTE this wording may change when final design is picked to be changed as still working in it***)
• Colours: white, black and gold (those are our website colours).
• I'd like the Highstride to really stand out.... I have included two fonts that I really like that I got off Brightstall Bazaar. However, feel free to suggest other fonts that you think cool or funky! NOTE: The pictures I have attached is mainly for the FONTS not for the background pictures. I am not that keen on background pictures as it can take away from the font - unless it is minimal
Should not have
• Too many different colours, I like slick, modern, clean. White, gold and black preferred as this is our website colour.
• NOTE: The pictures from Brightstall Bazaar I have attached are mainly for the FONTS not for the background pictures. I am not hugely keen on background pictures as it can take away from the font/message - unless the pictures are minimal but effective.

```html
<!DOCTYPE html>
<html lang="en">
<head>
<meta charset="utf-8">
<title>Highstride Flyer – Light and Dark</title>
<link rel="stylesheet" href="https://fonts.googleapis.com/css2?family=Oswald:wght@700&family=Lato:wght@400&family=Yellowtail&display=swap">
<style>
  :root {
    --gold: #c9a032;
    --gold-deep: #b38a22;
    --gold-pale: #f6e8a8;
    --ink: #1f1f1f;
    --grey-text: #555555;
    --paper: #ffffff;
    --paper-shade: #ececec;
    --charcoal: #3a3a3a;
    --charcoal-deep: #2e2e2e;
    --stage: #ebe7e1;
  }
  * { margin: 0; padding: 0; box-sizing: border-box; }
  html, body { width: 1200px; height: 1200px; overflow: hidden; }
  body {
    background: var(--stage);
    font-family: "Lato", sans-serif;
    position: relative;
  }
  .flyer {
    position: absolute;
    top: 212px;
    width: 548px;
    height: 776px;
    overflow: hidden;
    box-shadow: 0 3px 8px rgba(0,0,0,.25);
  }
  .flyer--light { left: 37px; background: linear-gradient(160deg, var(--paper) 0%, var(--paper-shade) 100%); color: var(--ink); }
  .flyer--dark { left: 616px; background: linear-gradient(160deg, var(--charcoal) 0%, var(--charcoal-deep) 100%); color: var(--paper); }

  .brand {
    position: absolute; top: 44px; left: 0; width: 100%;
    display: flex; justify-content: center; align-items: center; gap: 10px;
    font-size: 19px; letter-spacing: 2px;
  }
  .brand__mark { width: 12px; height: 12px; background: currentColor; }
  .flyer--light .brand { color: var(--grey-text); }
  .flyer--dark .brand { color: var(--gold); }

  .accent { position: absolute; left: 0; width: 548px; height: 10px; }
  .accent--top { top: 94px; }
  .accent--bottom { top: 362px; }

  .photo {
    position: absolute; top: 104px; left: 0; width: 548px; height: 256px;
    border-top: 3px solid var(--paper); border-bottom: 3px solid var(--paper);
    background: linear-gradient(100deg, #c9a88a 0%, #7a3a36 25%, #3c4a6a 55%, #8a8580 80%, #b9aa98 100%);
  }

  .headline {
    position: absolute; top: 398px; left: 0; width: 100%;
    text-align: center;
    font-family: "Oswald", sans-serif; font-weight: 700;
    font-size: 44px; line-height: 54px; letter-spacing: 1px;
    color: var(--gold);
    text-transform: uppercase;
  }
  .program-name {
    position: absolute; top: 510px; left: 0; width: 100%;
    text-align: center;
    font-family: "Yellowtail", cursive;
    font-size: 76px; line-height: 100px;
    color: var(--gold);
  }
  .services {
    position: absolute; top: 618px; left: 0; width: 100%;
    text-align: center; font-size: 24px;
  }
  .description {
    position: absolute; top: 666px; left: 24px; width: 500px;
    text-align: center; font-size: 14px; line-height: 17.5px;
  }

  .contact-bar { position: absolute; top: 742px; left: 0; width: 548px; height: 34px; }
  .contact-bar svg { position: absolute; inset: 0; }
  .contact-bar__links {
    position: absolute; inset: 0;
    display: flex; justify-content: center; align-items: center; gap: 18px;
    font-size: 11.5px; color: var(--ink);
    padding-right: 20px;
  }
  .contact-bar__item { display: flex; align-items: center; gap: 5px; }
</style>
</head>
<body>

<!-- Light edition -->
<section class="flyer flyer--light">
  <div class="brand"><span class="brand__mark"></span>MIRIAM BASKELL</div>
  <svg class="accent accent--top" viewBox="0 0 548 10"><polygon points="0,0 140,0 128,10 0,10" fill="var(--gold)"/></svg>
  <div class="photo" role="img" aria-label="Photo of a mentor reviewing documents with two colleagues at a table"></div>
  <svg class="accent accent--bottom" viewBox="0 0 548 10"><polygon points="432,0 548,0 548,10 422,10" fill="var(--gold)"/></svg>
  <h1 class="headline">Executive Digital<br>Sales Strategist</h1>
  <h2 class="program-name">Highstride</h2>
  <p class="services">Training, Mentoring</p>
  <p class="description">This is one of our highest in-demand programs and is based on a background and proven track record by Miriam in accelerating sales organisations and their people into stand out high performers.</p>
  <footer class="contact-bar">
    <svg viewBox="0 0 548 34" preserveAspectRatio="none">
      <rect width="548" height="34" fill="var(--gold)"/>
      <polygon points="100,0 126,0 106,34 80,34" fill="var(--gold-deep)"/>
      <polygon points="126,0 492,0 472,34 106,34" fill="var(--gold-pale)"/>
      <polygon points="492,0 516,0 496,34 472,34" fill="var(--gold-deep)"/>
      <rect y="31" width="548" height="3" fill="#111"/>
    </svg>
    <div class="contact-bar__links">
      <span class="contact-bar__item"><svg width="10" height="10" viewBox="0 0 10 10"><circle cx="5" cy="5" r="4.5" fill="#222"/><path d="M0.5 5h9M5 .5c2 2 2 7 0 9M5 .5c-2 2-2 7 0 9" stroke="var(--gold-pale)" stroke-width=".7" fill="none"/></svg>www.miriambaskell.example</span>
      <span class="contact-bar__item"><svg width="12" height="9" viewBox="0 0 12 9"><rect width="12" height="9" fill="#222"/><path d="M0.5 0.5 6 5l5.5-4.5" stroke="var(--gold-pale)" stroke-width="1" fill="none"/></svg>miriam@miriambaskell.example</span>
    </div>
  </footer>
</section>

<!-- Dark edition -->
<section class="flyer flyer--dark">
  <div class="brand"><span class="brand__mark"></span>MIRIAM BASKELL</div>
  <svg class="accent accent--top" viewBox="0 0 548 10"><polygon points="0,0 140,0 128,10 0,10" fill="var(--gold)"/></svg>
  <div class="photo" role="img" aria-label="Photo of a mentor reviewing documents with two colleagues at a table"></div>
  <svg class="accent accent--bottom" viewBox="0 0 548 10"><polygon points="432,0 548,0 548,10 422,10" fill="var(--gold)"/></svg>
  <h1 class="headline">Executive Digital<br>Sales Strategist</h1>
  <h2 class="program-name">Highstride</h2>
  <p class="services">Training, Mentoring</p>
  <p class="description">This is one of our highest in-demand programs and is based on a background and proven track record by Miriam in accelerating sales organisations and their people into stand out high performers.</p>
  <footer class="contact-bar">
    <svg viewBox="0 0 548 34" preserveAspectRatio="none">
      <rect width="548" height="34" fill="var(--gold)"/>
      <polygon points="100,0 126,0 106,34 80,34" fill="var(--gold-deep)"/>
      <polygon points="126,0 492,0 472,34 106,34" fill="var(--gold-pale)"/>
      <polygon points="492,0 516,0 496,34 472,34" fill="var(--gold-deep)"/>
      <rect y="31" width="548" height="3" fill="#111"/>
    </svg>
    <div class="contact-bar__links">
      <span class="contact-bar__item"><svg width="10" height="10" viewBox="0 0 10 10"><circle cx="5" cy="5" r="4.5" fill="#222"/><path d="M0.5 5h9M5 .5c2 2 2 7 0 9M5 .5c-2 2-2 7 0 9" stroke="var(--gold-pale)" stroke-width=".7" fill="none"/></svg>www.miriambaskell.example</span>
      <span class="contact-bar__item"><svg width="12" height="9" viewBox="0 0 12 9"><rect width="12" height="9" fill="#222"/><path d="M0.5 0.5 6 5l5.5-4.5" stroke="var(--gold-pale)" stroke-width="1" fill="none"/></svg>miriam@miriambaskell.example</span>
    </div>
  </footer>
</section>

</body>
</html>
```